Managed Service Provider need new business cards

We are a small Maanged Service Provider of IT Services and need a new fresh design for our business cards. We want something impossible, fun and professional :)
Our services has a large range, but we are always fun and make sure our customers both get their issue sorted and also feel like they are "catching up with an old friend".
All our cards in the past has always been all black, with red and we need something fresher.
The back of card, we would like just a small list of what we do i think, but if someone has a better idea, please do something cool with the back of the card:
Managed IT Services
Productivity Solutions
Data Backup and Recovery
IT System Maintenance
Managed IT Security
More details can be found on our website tqnetworks.com.au
Industry/Entity Type
It Company
Contact Information for Business Card
Name: Dwayne Falstrup
Title: Director
Phone: 03 6193 4827
Mobile: 0412 587 239
Email: dwayne@tqnetworks.com.au
Web: www.tqnetworks.com.au

```html
<!DOCTYPE html>
<html lang="en">
<head>
<meta charset="utf-8">
<title>TQ Networks – Business Card</title>
<link href="https://fonts.googleapis.com/css2?family=Roboto+Condensed:wght@400;700&display=swap" rel="stylesheet">
<style>
  :root {
    --brand-red: #ed1c24;
    --brand-red-deep: #c9151c;
    --charcoal: #414042;
    --paper: #ffffff;
    --backdrop: #8c8c8c;
  }
  html, body {
    margin: 0;
    padding: 0;
    width: 1125px;
    height: 1200px;
    overflow: hidden;
    background: var(--backdrop);
    font-family: "Roboto Condensed", "Arial Narrow", sans-serif;
  }
  .canvas {
    position: relative;
    width: 1125px;
    height: 1200px;
  }
  .card {
    position: absolute;
    left: 171px;
    width: 826px;
    height: 472px;
    overflow: hidden;
  }
  .card--front { top: 106px; background: var(--paper); }
  .card--back  { top: 640px; background: var(--brand-red); }

  .corner-panel {
    position: absolute;
    inset: 0;
    width: 100%;
    height: 100%;
  }

  .wordmark {
    position: absolute;
    left: 74px;
    top: 76px;
    margin: 0;
    font-weight: 700;
    font-size: 58px;
    letter-spacing: -1px;
    color: var(--brand-red);
    line-height: 1;
  }

  .contact {
    position: absolute;
    right: 35px;
    top: 262px;
    text-align: right;
    color: var(--paper);
  }
  .contact__name {
    margin: 0;
    font-weight: 700;
    font-size: 27px;
    color: var(--brand-red);
    line-height: 1.1;
  }
  .contact__title {
    margin: 2px 0 14px;
    font-size: 19px;
    line-height: 1.2;
  }
  .contact__list {
    list-style: none;
    margin: 0;
    padding: 0;
  }
  .contact__item {
    display: flex;
    justify-content: flex-end;
    align-items: center;
    gap: 9px;
    font-size: 19px;
    line-height: 23px;
  }
  .contact__icon {
    width: 14px;
    height: 14px;
    flex: none;
  }

  .back-mark {
    position: absolute;
    left: 0;
    right: 0;
    top: 150px;
    margin: 0;
    text-align: center;
    font-weight: 700;
    font-size: 86px;
    letter-spacing: -1px;
    color: var(--brand-red-deep);
    line-height: 1;
  }
  .services {
    position: absolute;
    left: 0;
    right: 0;
    top: 374px;
    margin: 0;
    padding: 0;
    list-style: none;
    text-align: center;
    color: var(--paper);
    font-size: 20px;
    line-height: 26px;
  }
  .services__row { display: block; }
  .services__tick {
    display: inline-block;
    width: 17px;
    height: 17px;
    vertical-align: -2px;
    margin: 0 2px;
  }
</style>
</head>
<body>
<main class="canvas">

  <section class="card card--front" aria-label="Business card front">
    <svg class="corner-panel" viewBox="0 0 826 472" aria-hidden="true">
      <polygon points="826,100 826,472 250,472" fill="var(--charcoal)"/>
      <line x1="215" y1="472" x2="826" y2="78" stroke="var(--brand-red)" stroke-width="8"/>
    </svg>

    <h1 class="wordmark">TQ NETWORKS</h1>

    <div class="contact">
      <p class="contact__name">Dwayne Falstrup</p>
      <p class="contact__title">Director</p>
      <ul class="contact__list">
        <li class="contact__item">03 6193 4827
          <svg class="contact__icon" viewBox="0 0 16 16" aria-hidden="true"><path d="M3.5 1.5l2.5 0 1 3.5-1.8 1.3c.9 1.9 2.3 3.3 4.2 4.2l1.3-1.8 3.5 1v2.5c0 .9-.8 1.6-1.7 1.5C6.8 13.3 2.7 9.2 2 3.2 1.9 2.3 2.6 1.5 3.5 1.5z" fill="var(--brand-red)"/></svg>
        </li>
        <li class="contact__item">0412 587 239
          <svg class="contact__icon" viewBox="0 0 16 16" aria-hidden="true"><rect x="4" y="1" width="8" height="14" rx="1.5" fill="none" stroke="var(--brand-red)" stroke-width="1.8"/><circle cx="8" cy="12.3" r="0.9" fill="var(--brand-red)"/></svg>
        </li>
        <li class="contact__item">dwayne@tqnetworks.com.au
          <svg class="contact__icon" viewBox="0 0 16 16" aria-hidden="true"><rect x="1" y="3.5" width="14" height="9.5" rx="1" fill="var(--brand-red)"/><path d="M1.5 4.2L8 9l6.5-4.8" fill="none" stroke="var(--charcoal)" stroke-width="1.2"/></svg>
        </li>
        <li class="contact__item">www.tqnetworks.com.au
          <svg class="contact__icon" viewBox="0 0 16 16" aria-hidden="true"><circle cx="8" cy="8" r="7" fill="var(--brand-red)"/><path d="M1 8h14M8 1c-3 3.5-3 10.5 0 14M8 1c3 3.5 3 10.5 0 14" fill="none" stroke="var(--charcoal)" stroke-width="1"/></svg>
        </li>
      </ul>
    </div>
  </section>

  <section class="card card--back" aria-label="Business card back">
    <p class="back-mark">TQ NETWORKS</p>
    <ul class="services">
      <li class="services__row">Managed IT Services
        <svg class="services__tick" viewBox="0 0 16 16" aria-hidden="true"><circle cx="8" cy="8" r="8" fill="var(--paper)"/><path d="M4.3 8.3l2.5 2.4 4.9-5" fill="none" stroke="var(--brand-red)" stroke-width="2"/></svg>
        Productivity Solutions</li>
      <li class="services__row">Data Backup &amp; Recovery
        <svg class="services__tick" viewBox="0 0 16 16" aria-hidden="true"><circle cx="8" cy="8" r="8" fill="var(--paper)"/><path d="M4.3 8.3l2.5 2.4 4.9-5" fill="none" stroke="var(--brand-red)" stroke-width="2"/></svg>
        IT System Maintenance
        <svg class="services__tick" viewBox="0 0 16 16" aria-hidden="true"><circle cx="8" cy="8" r="8" fill="var(--paper)"/><path d="M4.3 8.3l2.5 2.4 4.9-5" fill="none" stroke="var(--brand-red)" stroke-width="2"/></svg>
        Managed IT Security</li>
    </ul>
  </section>

</main>
</body>
</html>
```